Marlowen

I'm looking for business cards with the logo I've attached. I don't have an specific idea in mind and open to anything. All the usual info will be involved. Name, position in company, nr, email, address

```html
<!DOCTYPE html>
<html lang="en">
<head>
<meta charset="UTF-8">
<title>Marlowen Designs – Business Cards</title>
<link href="https://fonts.googleapis.com/css2?family=Montserrat:wght@400;600;700&family=Arimo:wght@400&display=swap" rel="stylesheet">
<style>
  :root {
    --backdrop: #e4e4e2;
    --paper: #f7f7f5;
    --navy: #13294a;
    --navy-deep: #0d1f3a;
    --gold: #e3a72f;
    --edge-gold: #c79a2a;
    --ink-grey: #6a6a6a;
    --rule-grey: #8a8a8a;
  }
  * { box-sizing: border-box; margin: 0; padding: 0; }
  html, body { width: 1200px; height: 801px; overflow: hidden; }
  body {
    background: var(--backdrop);
    display: flex;
    align-items: center;
    justify-content: center;
    gap: 56px;
    font-family: "Arimo", Arial, sans-serif;
  }
  .card {
    width: 525px;
    height: 300px;
    border-bottom: 4px solid var(--edge-gold);
    border-right: 2px solid var(--edge-gold);
    box-shadow: 0 10px 24px rgba(0,0,0,0.12);
    position: relative;
    overflow: hidden;
  }
  /* Front */
  .card-front { background: var(--paper); padding: 0 30px; }
  .brand {
    position: absolute;
    top: 58px;
    right: 32px;
    display: flex;
    align-items: center;
    gap: 10px;
  }
  .brand-dot { width: 14px; height: 14px; border-radius: 50%; background: var(--navy); }
  .brand-name {
    font-family: "Montserrat", sans-serif;
    font-weight: 700;
    color: var(--gold);
    font-size: 30px;
    letter-spacing: 1px;
    line-height: 1;
  }
  .person {
    position: absolute;
    left: 30px;
    top: 120px;
  }
  .person-name {
    font-family: "Montserrat", sans-serif;
    font-weight: 700;
    color: var(--gold);
    font-size: 17px;
    letter-spacing: 0.5px;
  }
  .person-role { color: var(--ink-grey); font-size: 14px; margin-top: 2px; }
  .divider {
    position: absolute;
    left: 30px;
    right: 30px;
    top: 170px;
    height: 1px;
    background: var(--rule-grey);
  }
  .contacts {
    position: absolute;
    left: 30px;
    top: 186px;
    list-style: none;
    display: flex;
    flex-direction: column;
    gap: 7px;
  }
  .contacts li {
    display: flex;
    align-items: center;
    gap: 9px;
    color: var(--ink-grey);
    font-size: 14px;
  }
  .contacts svg { width: 14px; height: 14px; fill: var(--gold); flex: none; }
  .address {
    position: absolute;
    right: 30px;
    top: 190px;
    text-align: right;
    color: var(--ink-grey);
    font-size: 14px;
    line-height: 1.35;
  }
  /* Back */
  .card-back {
    background: linear-gradient(135deg, var(--navy) 0%, var(--navy-deep) 70%, #1a3660 100%);
    display: flex;
    align-items: center;
    justify-content: center;
    gap: 14px;
  }
  .card-back .brand-dot { width: 20px; height: 20px; background: var(--gold); }
  .card-back .brand-name { font-size: 40px; }
</style>
</head>
<body>
  <section class="card card-front" aria-label="Business card front">
    <div class="brand">
      <span class="brand-dot"></span>
      <span class="brand-name">MARLOWEN DESIGNS</span>
    </div>
    <div class="person">
      <p class="person-name">ELIAS BRANDT</p>
      <p class="person-role">Manager</p>
    </div>
    <div class="divider"></div>
    <ul class="contacts">
      <li>
        <svg viewBox="0 0 24 24" aria-hidden="true"><path d="M6.6 10.8a15.2 15.2 0 0 0 6.6 6.6l2.2-2.2a1 1 0 0 1 1-.25 11.4 11.4 0 0 0 3.6.57 1 1 0 0 1 1 1V20a1 1 0 0 1-1 1A17 17 0 0 1 3 4a1 1 0 0 1 1-1h3.5a1 1 0 0 1 1 1c0 1.25.2 2.46.57 3.6a1 1 0 0 1-.25 1z"/></svg>
        555-018-4420
      </li>
      <li>
        <svg viewBox="0 0 24 24" aria-hidden="true"><path d="M2 5h20v14H2zm2 2v.5l8 5 8-5V7l-8 5z"/></svg>
        elias@marlowenmail.com
      </li>
      <li>
        <svg viewBox="0 0 24 24" aria-hidden="true"><circle cx="12" cy="12" r="10"/></svg>
        www.marlowen.com
      </li>
    </ul>
    <p class="address">Your address, city<br>state, ZIP 0000</p>
  </section>

  <section class="card card-back" aria-label="Business card back">
    <span class="brand-dot"></span>
    <span class="brand-name">MARLOWEN DESIGNS</span>
  </section>
</body>
</html>
```